Lantern Stewardship Frame

I am looking for a graphic design of the attached leadership model. The colors and design can be altered in any manner that brings the model alive version of the house model.

```html
<!DOCTYPE html>
<html lang="en">
<head>
<meta charset="utf-8">
<title>Lantern Stewardship Frame</title>
<link href="https://fonts.googleapis.com/css2?family=Open+Sans:wght@400;600;700&display=swap" rel="stylesheet">
<style>
:root{
  --gold:#FFC000;
  --gold-text:#F4B400;
  --sky:#0A9AD0;
  --blue:#4472C4;
  --blue-pale:#D9E0EC;
  --orange:#ED7D31;
  --orange-pale:#F8D9C4;
  --green:#70AD47;
  --green-pale:#D5E7C8;
  --navy:#203864;
  --ghost:#DCDCDC;
  --white:#FFFFFF;
}
*{margin:0;padding:0;box-sizing:border-box}
html,body{width:1200px;height:675px;overflow:hidden}
body{font-family:"Open Sans",Arial,sans-serif;background:#fff}
.canvas{position:relative;width:1200px;height:675px;overflow:hidden;
  background:linear-gradient(180deg,#FFFFFF 0%,#FFFFFF 38%,#EFEFEF 100%)}
.abs{position:absolute}
.growth-arrows{left:0;top:0}
.title-box{left:0;top:67px;width:237px;height:75px;background:var(--gold);border-radius:0 4px 4px 0;
  color:var(--white);font-size:37px;font-weight:600;letter-spacing:.5px;line-height:75px;padding-left:32px}
.tagline{left:32px;top:165px;width:215px;color:var(--gold-text);font-size:15px;font-weight:600;line-height:18.2px}
.band{background:var(--sky);color:var(--white);border-radius:4px;display:flex;align-items:center;justify-content:center;
  font-size:13px;font-weight:600;box-shadow:0 2px 4px rgba(0,0,0,.15)}
.band.outer{left:321px;top:139px;width:817px;height:31px}
.band.inner{left:317px;top:487px;width:821px;height:36px}
.col-head{height:42px;border-radius:4px;color:var(--white);font-size:10.6px;font-weight:600;text-align:center;
  line-height:14px;display:flex;align-items:center;justify-content:center;box-shadow:0 2px 4px rgba(0,0,0,.15)}
.pale{position:absolute}
.spine{position:absolute;width:4px}
.dot{position:absolute;width:22px;height:22px;border-radius:50%}
.tick{position:absolute;height:4px;width:14px}
.item{position:absolute;border-radius:4px;color:var(--white);font-size:10px;font-weight:600;line-height:12px;
  display:flex;align-items:center;box-shadow:0 2px 4px rgba(0,0,0,.15)}
.org .col-head,.org .item,.org .dot,.org .spine,.org .tick{background:var(--blue)}
.org .pale{background:var(--blue-pale)}
.org .item{left:343px;width:179px;height:45px;padding:0 11px}
.inter .col-head,.inter .item,.inter .dot,.inter .spine,.inter .tick{background:var(--orange)}
.inter .pale{background:var(--orange-pale)}
.inter .item{left:647px;width:174px;height:35px;justify-content:center;text-align:center;padding:0 8px}
.pers .col-head,.pers .item,.pers .dot,.pers .spine,.pers .tick{background:var(--green)}
.pers .pale{background:var(--green-pale)}
.pers .item{left:964px;width:172px;height:32px;padding:0 11px}
.shift-arrow{position:absolute}
.pill{position:absolute;width:255px;height:29px;background:var(--sky);border-radius:3px;color:var(--white);
  font-size:11.3px;font-weight:600;display:flex;align-items:center;justify-content:center;box-shadow:0 2px 4px rgba(0,0,0,.15)}
.pill .go{position:absolute;left:6px;top:4.5px;width:20px;height:20px}
.footer{left:0;top:639px;width:1200px;height:36px;background:var(--navy)}
.footer-url{right:69px;top:13px;color:var(--white);font-size:9px}
</style>
</head>
<body>
<div class="canvas">
  <svg class="abs growth-arrows" width="320" height="675" viewBox="0 0 320 675" aria-hidden="true">
    <g fill="var(--ghost)">
      <polygon points="70,453 114,521 96,521 96,639 44,639 44,521 26,521"/>
      <polygon points="252,453 296,521 278,521 278,639 226,639 226,521 208,521"/>
      <polygon points="160,321 226,426 191,426 191,639 130,639 130,426 94,426"/>
    </g>
  </svg>

  <div class="abs title-box">LANTERN</div>
  <p class="abs tagline">FOSTER CONTAGIOUS SUCCESS THROUGH PEOPLE, RELATIONSHIPS AND A SHARED VISION</p>

  <div class="abs band outer">OUTER (IMPACT) STRATEGIES</div>

  <section class="org">
    <div class="pale" style="left:323px;top:226px;width:186px;height:248px"></div>
    <div class="spine" style="left:320px;top:220px;height:242px"></div>
    <div class="abs col-head" style="left:321px;top:184px;width:202px">ORGANIZATION LEVEL<br>WINS THEORY</div>
    <div class="dot" style="left:311px;top:251px"></div><div class="tick" style="left:330px;top:261px"></div>
    <div class="dot" style="left:311px;top:314px"></div><div class="tick" style="left:330px;top:324px"></div>
    <div class="dot" style="left:311px;top:378px"></div><div class="tick" style="left:330px;top:388px"></div>
    <div class="dot" style="left:311px;top:441px"></div><div class="tick" style="left:330px;top:451px"></div>
    <div class="item" style="top:241px">Develop concrete outcomes, and visible results</div>
    <div class="item" style="top:303px">Foster in-depth changes, and new practices</div>
    <div class="item" style="top:366px">Have a micro, interpersonal or local impact</div>
    <div class="item" style="top:430px">Cultivate positive judgement, and shared ambition</div>
  </section>

  <svg class="shift-arrow" style="left:554px;top:292px" width="72" height="75" viewBox="0 0 72 75" aria-hidden="true">
    <polygon points="0,37.5 44,0 44,17 72,17 72,58 44,58 44,75" fill="var(--orange-pale)"/>
  </svg>

  <section class="inter">
    <div class="pale" style="left:626px;top:226px;width:180px;height:249px"></div>
    <div class="spine" style="left:623px;top:220px;height:244px"></div>
    <div class="abs col-head" style="left:623px;top:184px;width:197px">INTERPERSONAL LEVEL<br>HEART LISTENING</div>
    <div class="dot" style="left:614px;top:246px"></div><div class="tick" style="left:633px;top:255px"></div>
    <div class="dot" style="left:614px;top:296px"></div><div class="tick" style="left:633px;top:305px"></div>
    <div class="dot" style="left:614px;top:346px"></div><div class="tick" style="left:633px;top:355px"></div>
    <div class="dot" style="left:614px;top:395px"></div><div class="tick" style="left:633px;top:404px"></div>
    <div class="dot" style="left:614px;top:445px"></div><div class="tick" style="left:633px;top:454px"></div>
    <div class="item" style="top:240px">Ask open-ended questions</div>
    <div class="item" style="top:289px">Affirm someone’s strengths, efforts and past success</div>
    <div class="item" style="top:339px">Reflect back what is shared for confirmation</div>
    <div class="item" style="top:389px">Summarize key points to gain insights</div>
    <div class="item" style="top:439px">Share and develop mutual expertise</div>
  </section>

  <svg class="shift-arrow" style="left:856px;top:289px" width="84" height="81" viewBox="0 0 84 81" aria-hidden="true">
    <polygon points="0,40.5 47,0 47,18 84,18 84,63 47,63 47,81" fill="var(--green-pale)"/>
  </svg>

  <section class="pers">
    <div class="pale" style="left:940px;top:226px;width:181px;height:249px"></div>
    <div class="spine" style="left:937px;top:220px;height:240px"></div>
    <div class="abs col-head" style="left:936px;top:185px;width:200px">PERSONAL LEVEL<br>INSIGHT DIALOGUE</div>
    <div class="dot" style="left:928px;top:246px"></div><div class="tick" style="left:947px;top:255px"></div>
    <div class="dot" style="left:928px;top:287px"></div><div class="tick" style="left:947px;top:296px"></div>
    <div class="dot" style="left:928px;top:327px"></div><div class="tick" style="left:947px;top:336px"></div>
    <div class="dot" style="left:928px;top:368px"></div><div class="tick" style="left:947px;top:377px"></div>
    <div class="dot" style="left:928px;top:408px"></div><div class="tick" style="left:947px;top:417px"></div>
    <div class="dot" style="left:928px;top:448px"></div><div class="tick" style="left:947px;top:457px"></div>
    <div class="item" style="top:241px">Pause</div>
    <div class="item" style="top:282px">Relax</div>
    <div class="item" style="top:322px">Open</div>
    <div class="item" style="top:363px">Attune to Emergence</div>
    <div class="item" style="top:403px">Listen Deeply</div>
    <div class="item" style="top:443px">Speak the Truth</div>
  </section>

  <div class="abs band inner">INNER (WELLBEING) STRATEGIES</div>

  <svg width="0" height="0" style="position:absolute" aria-hidden="true">
    <symbol id="go-icon" viewBox="0 0 20 20">
      <circle cx="10" cy="10" r="10" fill="#fff"/>
      <polyline points="8,5.5 12.5,10 8,14.5" fill="none" stroke="var(--sky)" stroke-width="2.4" stroke-linecap="round" stroke-linejoin="round"/>
    </symbol>
  </svg>

  <div class="pill" style="left:317px;top:539px"><svg class="go"><use href="#go-icon"/></svg>PHYSICAL FITNESS</div>
  <div class="pill" style="left:317px;top:574px"><svg class="go"><use href="#go-icon"/></svg>NUTRITION</div>
  <div class="pill" style="left:602px;top:539px"><svg class="go"><use href="#go-icon"/></svg>HEART RATE VARIABILITY</div>
  <div class="pill" style="left:602px;top:574px"><svg class="go"><use href="#go-icon"/></svg>NEUROFEEDBACK</div>
  <div class="pill" style="left:883px;top:539px"><svg class="go"><use href="#go-icon"/></svg>ISLAND HOPPIN CLUB</div>
  <div class="pill" style="left:883px;top:574px"><svg class="go"><use href="#go-icon"/></svg>VIDEO GAMING CLUB</div>

  <div class="abs footer"></div>
  <div class="abs footer-url">www.lanternframe.org</div>
</div>
</body>
</html>
```